Capability statement graphic design documement

We have written a capability statement for our training business, we would like someone to really make it professional and stand out.

Target Market(s)

Engineering, ports and mining companies

Industry/Entity Type

Coal Mining

Font styles to use
Sans Serif

Colors
9bcb3c

Requirements
Must have
• Very good visual designs.
I have included a couple of example such as the Orvo Dune capability statement which has good designs.
Our colours are green, black, white, grey. Our logos are uploaded.

```html
<!DOCTYPE html>
<html lang="en">
<head>
<meta charset="utf-8">
<title>NQFT Capability Statement – About Us &amp; Key Personnel</title>
<link href="https://fonts.googleapis.com/css2?family=Source+Sans+3:ital,wght@0,400;0,600;0,700;1,600;1,700&display=swap" rel="stylesheet">
<style>
:root{
  --green:#1a9a3c;
  --lime:#9bcb3c;
  --pale:#e9f3d9;
  --band:#dcebc4;
  --ink:#3a3a3a;
  --rule:#6f6f6f;
  --paper:#ffffff;
}
*{box-sizing:border-box;margin:0;padding:0}
html,body{width:1200px;height:849px;overflow:hidden;background:var(--paper)}
body{font-family:"Source Sans 3",Arial,sans-serif;color:var(--ink);position:relative}
.spread{position:absolute;inset:0;width:1200px;height:849px;overflow:hidden}
.corner{position:absolute;top:0}
.corner--left{left:0}
.corner--right{right:0}
.fold{position:absolute;left:600px;top:0;width:1px;height:849px;background:var(--rule)}
.section-title{position:absolute;font-size:14.5px;font-weight:400;color:#3a3a3a;line-height:15px;height:15px}
.section-title span{display:inline-block;background:var(--band);padding:0 16px 0 4px;clip-path:polygon(0 0,88% 0,100% 100%,0 100%)}
.section-title::after{content:"";position:absolute;left:0;right:0;bottom:0;height:1px;background:var(--band)}
.about-title{left:127px;top:47px;width:437px}
.personnel-title{left:737px;top:48px;width:361px}
.doc-label{position:absolute;left:996px;top:25px;font-size:9.6px;font-weight:700;color:var(--green)}
.doc-bar{position:absolute;left:1120px;top:27px;width:80px;height:9px;background:var(--green);clip-path:polygon(8px 0,100% 0,100% 100%,0 100%)}

.about{position:absolute;left:127px;top:70px;width:437px;font-size:8.4px;line-height:10.9px}
.about p{margin-bottom:6px;text-align:justify}
.about .hang{padding-left:22px;text-indent:-22px}
.about .inset{padding-left:23px}
.about ul{list-style:none;margin:4px 0 5px 25px}
.about li{position:relative;padding-left:11px;line-height:12.65px}
.about li::before{content:"";position:absolute;left:0;top:5px;width:3px;height:3px;border-radius:50%;background:var(--green)}
.about ul.facility li{line-height:9.9px;margin-bottom:3px;text-align:left}
.about ul.facility li::before{top:4px}
.about a{color:#222;text-decoration:none}

.pull-quote{position:absolute;left:49px;width:92px;background:var(--band);color:var(--green);font-weight:600;font-size:8.3px;line-height:10.9px;text-align:center;padding:7px 5px}
.pull-quote em{font-style:italic}
.quote-one{top:119px;height:102px}
.quote-two{top:520px;height:77px;padding-top:12px}

.profile{position:absolute;left:731px;width:368px;background:var(--pale);border:1.2px solid var(--lime);font-size:7.6px;line-height:9.7px;padding:0 6px}
.profile-one{top:74px;height:348px}
.profile-two{top:432px;height:345px}
.profile h2{font-size:11.4px;font-style:italic;font-weight:700;color:var(--green);line-height:14px}
.profile h3{font-size:8.3px;font-weight:600;color:#2e2e2e;margin:9px 0 2px}
.profile .indent{padding-left:11px}
.profile ul{list-style:none}
.profile li{position:relative;padding-left:12px;line-height:11.5px}
.profile li::before{content:"";position:absolute;left:1px;top:4.5px;width:2.6px;height:2.6px;border-radius:50%;background:var(--green)}
.profile .sub{display:block;padding-left:9px;line-height:9.7px}
.profile b{font-weight:700;color:#222}
.portrait{position:absolute;width:84px;height:84px;border-radius:50%;border:1.2px solid var(--lime);padding:2.5px;background:#fff}
.portrait span{display:block;width:100%;height:100%;border-radius:50%;background:linear-gradient(180deg,#dcdcd8 0%,#d2cfc9 55%,#e88a2e 80%,#e67a1e 100%)}
.portrait-one{left:660px;top:69px}
.portrait-two{left:662px;top:429px}
</style>
</head>
<body>
<div class="spread">
  <svg class="corner corner--left" width="120" height="80" viewBox="0 0 120 80" aria-hidden="true">
    <defs><linearGradient id="limeFadeL" x1="0" y1="0" x2="1" y2="1"><stop offset="0" stop-color="#c6df95"/><stop offset="1" stop-color="#8fc238"/></linearGradient></defs>
    <path d="M0 0H113A113 77 0 0 1 0 77Z" fill="#e3efcf"/>
    <path d="M0 0H108A108 71 0 0 1 0 71Z" fill="url(#limeFadeL)"/>
  </svg>
  <svg class="corner corner--right" width="120" height="80" viewBox="0 0 120 80" aria-hidden="true">
    <defs><linearGradient id="limeFadeR" x1="1" y1="0" x2="0" y2="1"><stop offset="0" stop-color="#c6df95"/><stop offset="1" stop-color="#8fc238"/></linearGradient></defs>
    <path d="M120 0H7A113 77 0 0 0 120 77Z" fill="#e3efcf"/>
    <path d="M120 0H12A108 71 0 0 0 120 71Z" fill="url(#limeFadeR)"/>
  </svg>
  <div class="fold"></div>

  <h1 class="section-title about-title"><span>About Us</span></h1>
  <div class="about">
    <p>Formed in 2019, NQ Field Training (NQFT) was borne from a vision to deliver superior training and assessment services that strives to exceed the expectations of our customers.</p>
    <p class="hang">As specialists in the field of high risk training and assessment services, NQFT is well equipped to undertake a range of High Risk Work Licence (HRWL) services including:</p>
    <ul>
      <li>Forklift</li><li>Elevating work platform (EWP)</li><li>Dogging</li><li>Basic rigging</li><li>Intermediate rigging</li><li>Non-slewing mobile crane</li><li>Open crane</li>
    </ul>
    <p style="text-indent:22px;margin-top:7px">In addition to HRWL services, we provide a comprehensive range of Resource Infrastructure Industry (RII) courses including:</p>
    <ul>
      <li>Forklift</li><li>Elevating work platform (EWP)</li><li>Gantry/overhead crane</li><li>Telescopic materials handler (telehandler)</li><li>Vehicle loading crane (VLC)</li><li>Dogging</li><li>Conduct lifting operations</li><li>Non-slewing mobile crane</li><li>Work safely at heights</li><li>Confined space</li>
    </ul>
    <p>We have the expertise to undertake a range of supplementary services. These include large group training, training package design and development, Training Needs Analysis, providing advice on High Risk training requirements, Verification of Competency (VOC), familiarisation on machines/equipment plus other support services.</p>
    <p>NQFT has a purpose-built facility at the Marlin Harbour which includes:</p>
    <ul class="facility">
      <li>comfortable modern training rooms with generous sized desks, large flat screen LED TV and soundproofing between rooms</li>
      <li>a custom-made structure that is utilised for basic rigging, intermediate rigging, elevating work platform and working at heights. The working at heights facility allows for the use of specific equipment such as inertia reels, dual hook ups, retractable lanyards, LiftSafe Kits and to demonstrate the use of emergency release straps</li>
    </ul>
    <p class="hang">This location at the Marlin Harbour provides an abundance of space to practice and learn in a controlled yet realistic work environment. This naturally influences the person to conduct a more thorough risk assessment, thus enforcing their understanding of risk management and appropriate control strategies.</p>
    <p class="inset">As well as our own facility, NQFT can conduct most training on site – in town or a mine site.</p>
    <p class="inset">We currently have three trainer/assessors plus a consultant to provide a range of training and support services. Our trainers are knowledgeable, experienced, and importantly, professional and respectful. All our trainers hold the required licences, competencies, and insurances to perform training and assessment services. We encourage continual learning and development through meetings, Professional Development activities and networking.</p>
    <p>NQ Field Training works in partnership with SiteLearn (RTO No. 40210).</p>
    <p>If you would like further information about our courses, our people or to make contact,<br>please visit our website <a href="#">www.nqfieldtraining.com.au</a></p>
  </div>
  <aside class="pull-quote quote-one">“Our goal is to <em>connect</em> great trainers with quality resources in a professional environment for our customers, ensuring a training experience above any other.”</aside>
  <aside class="pull-quote quote-two">“Not all trainers are the same - selecting the <em>right kind</em> of trainer is a crucial aspect of our business.”</aside>

  <div class="doc-label">NQFT Capability Statement</div>
  <div class="doc-bar"></div>
  <h1 class="section-title personnel-title"><span>Key Personnel</span></h1>

  <section class="profile profile-one">
    <h2 style="margin:3px 0 0 11px">Orvo Dune – Director/Business Manager</h2>
    <h3 class="indent" style="margin-top:8px">Key Responsibilities</h3>
    <p class="indent">Orvo drives the overall direction of the business focusing on building relationships and networks within the industry. Orvo manages all aspects of administration, finances, legislative requirements, and marketing.</p>
    <h3 class="indent" style="margin-top:9px">Personal Strengths</h3>
    <ul>
      <li>Strong communication and interpersonal skills</li>
      <li>Always has time to invest in others</li>
      <li>Logical and systematic</li>
      <li>Good understanding of training required for mining, ports and civil industries</li>
    </ul>
    <h3>Qualifications</h3>
    <ul>
      <li>Bachelor of Business (Coastal University)</li>
      <li>Graduate Certificate in Learning Technology (Coastal University)</li>
      <li>Graduate Diploma in Secondary Education (Coastal University)</li>
      <li>Diploma in OHS</li>
      <li>Certificate IV in TAE</li>
    </ul>
    <h3>Experience</h3>
    <p>Some of Orvo’s recent experience in her 12 years in education and learning and development:</p>
    <ul style="margin-top:2px">
      <li>Training Officer at <b>Northbay Coal Terminal</b><span class="sub">Seconded into Training Advisor position to coordinate the training requirements for Business Services/ Business Improvement</span></li>
      <li>Training Coordinator at <b>Ridgeline’s Flat Creek Mine</b><span class="sub">Part of a team who designed a site-wide Training Needs Analysis and online document library<br>Managed the training requirements for the Maintenance and CHPP departments</span></li>
      <li>Trainer for <b>Veritas Safety Australia</b><span class="sub">Part of a team who designed the initial 3-day Standard 11 course<br>Delivered generic induction training across the region</span></li>
      <li>Secondary school teacher for <b>Regional Education Board</b></li>
    </ul>
  </section>
  <div class="portrait portrait-one" role="img" aria-label="Portrait photo of Orvo Dune in orange high-visibility work shirt"><span></span></div>

  <section class="profile profile-two">
    <h2 style="margin:14px 0 0 13px">Tam Reyes – Director/Trainer Assessor</h2>
    <h3 style="margin:9px 0 2px 13px">Key Responsibilities</h3>
    <p style="padding-left:13px">Tam drives the overall direction of the business focusing on building relationships and networks within the industry. Tam is a High Risk Work Licence Accredited Trainer/Assessor, performing training and assessment in classes LF, WP, DG, RB, CN and C0.</p>
    <h3 style="margin-top:10px">Personal Strengths</h3>
    <ul>
      <li>Strong communication and interpersonal skills</li>
      <li>Can make the hard decisions and follow through with implementation</li>
      <li>Driven and strong willed yet people orientated</li>
      <li>Focused</li>
    </ul>
    <h3>Qualifications</h3>
    <ul>
      <li>High Risk Work Licence – LF, WP, DG, RB, RI, CN, CT, C0</li>
      <li>WHSQ Accredited Trainer/Assessor – LF, WP, DG, RB, CN, C0</li>
      <li>Certificate IV in TAE</li>
    </ul>
    <h3>Experience</h3>
    <p>Some of Tam’s recent experience in his 18 years in mining, ports and civil construction including rigging, crane operating and learning and development:</p>
    <ul style="margin-top:4px">
      <li style="line-height:12.5px">Trainer/High Risk Work Licence Trainer and Assessor at <b>NQ Field Training</b></li>
      <li style="line-height:12.5px">Training Coordinator/Trainer at <b>Basalt’s Western Mine</b></li>
      <li style="line-height:12.5px">Special Projects (Cranes and Rigging) at <b>Kuma Ridge Mine, PNG</b><span class="sub" style="padding-left:6px;line-height:12.5px">Established a training department within the company<br>Designed and implemented a Training Needs Analysis<br>Coordinate large special projects in cranes and rigging</span></li>
      <li style="line-height:12.5px">Crane operator for <b>Harwood Civil (Point Expansion – PX)</b><span class="sub" style="padding-left:8px;line-height:10px">Operated 750t Krantech crawler crane</span></li>
    </ul>
  </section>
  <div class="portrait portrait-two" role="img" aria-label="Portrait photo of Tam Reyes in orange high-visibility work shirt"><span></span></div>
</div>
</body>
</html>
```